Fancy&Artistic design bussiness card!

I want a business card for myself.I'm a cinephile.Love watching SF(especially distopia one),Cult(mostly from midnight movies),Chivalrous story film. My favorite film for example,○Lantern (directed by morris Quenby)○lurkers○queen of lakes○wild copper lane(Japanese film)○velvet harbor○steelwarden ○specter of bellhaven ○TOMUZ○the revenge of the buried crowd ○El topoAnd I also love modern art. I love their way of using colors(Bert Lindqvam,Silas Porrend, Calvimurra,etc..)I want to get a business card which is full of creativity, uniqueness and humor(related to movie or art would be much better).I will be very pleased if you would meet my expectations. Thank you.
Movie
Name: HIROKAZU ENOMOTOAddress: 207 W85th Street #3106 NewYork,NY 10024e-mail: Tasuga@qelvmail.com

```html
<!DOCTYPE html>
<html lang="en">
<head>
<meta charset="UTF-8">
<title>Takemura Suginaka — Business Card</title>
<link href="https://fonts.googleapis.com/css2?family=Cinzel:wght@400;600&family=Arimo:wght@400&display=swap" rel="stylesheet">
<style>
  :root {
    --page-bg: #e9e7e3;
    --card-black: #0e0e0f;
    --card-dark: #1d1e20;
    --card-glow: #8e9094;
    --silver: #d9dbde;
    --silver-dim: #7c7f84;
    --text-light: #e6e7e9;
    --text-soft: #c3c5c8;
  }
  * { box-sizing: border-box; margin: 0; padding: 0; }
  html, body {
    width: 1200px; height: 848px; overflow: hidden;
    background: var(--page-bg);
  }
  .sheet {
    width: 1200px; height: 848px;
    display: flex; flex-direction: column; align-items: center; justify-content: center;
    gap: 30px;
  }
  .card {
    position: relative;
    width: 665px; height: 380px;
    border-radius: 26px;
    overflow: hidden;
    background:
      radial-gradient(ellipse 42% 38% at var(--glow-x, 55%) var(--glow-y, 40%), var(--card-glow) 0%, #4a4b4e 38%, transparent 80%),
      linear-gradient(160deg, var(--card-dark) 0%, var(--card-black) 70%);
    box-shadow: 0 10px 28px rgba(0,0,0,0.28);
  }
  .card--front { --glow-x: 52%; --glow-y: 40%; }
  .card--back  { --glow-x: 50%; --glow-y: 42%; }

  .holder-name {
    position: absolute;
    font-family: "Cinzel", serif;
    font-weight: 600;
    letter-spacing: 1px;
    color: var(--card-black);
    -webkit-text-stroke: 1px var(--silver);
    text-shadow: 0 0 6px rgba(255,255,255,0.35);
    white-space: nowrap;
  }
  .card--front .holder-name { left: 70px; top: 118px; font-size: 28px; }
  .card--back .holder-name {
    right: 40px; top: 92px; font-size: 26px;
    color: var(--text-light); -webkit-text-stroke: 0; font-weight: 400;
  }

  .holder-title {
    position: absolute; right: 40px; top: 128px;
    font-family: "Arimo", sans-serif; font-size: 13px; letter-spacing: 1px;
    color: var(--text-soft);
  }

  .contact {
    position: absolute; right: 62px; top: 162px;
    font-family: "Arimo", sans-serif; font-size: 15px; line-height: 1.75;
    color: var(--text-soft); text-align: right;
  }
  .contact__email { display: inline-flex; align-items: center; gap: 8px; }
  .contact__icon { width: 14px; height: 11px; }

  .film-art {
    position: absolute;
    border-radius: 40px;
    background: radial-gradient(ellipse at 45% 45%, var(--silver) 0%, var(--silver-dim) 35%, #2a2b2e 75%, transparent 100%);
    opacity: 0.85;
  }
  .card--front .film-art { left: 365px; top: 150px; width: 270px; height: 200px; }
  .card--back .film-art { left: 35px; top: 165px; width: 250px; height: 195px; }
</style>
</head>
<body>
  <main class="sheet">
    <section class="card card--front" aria-label="Card front">
      <h1 class="holder-name">TAKEMURA SUGINAKA</h1>
      <div class="film-art" role="img" aria-label="Silver curling strip of movie film"></div>
    </section>

    <section class="card card--back" aria-label="Card back">
      <h2 class="holder-name">TAKEMURA SUGINAKA</h2>
      <p class="holder-title">Your Title</p>
      <address class="contact">
        318 E62nd Street<br>
        #4217 NewYork,NY 10031<br>
        <span class="contact__email">Tasuga@qelvmail.com
          <svg class="contact__icon" viewBox="0 0 14 11" aria-hidden="true">
            <rect x="0.5" y="0.5" width="13" height="10" rx="1" fill="none" stroke="#c3c5c8"/>
            <path d="M0.8 1 L7 6 L13.2 1" fill="none" stroke="#c3c5c8"/>
          </svg>
        </span>
      </address>
      <div class="film-art" role="img" aria-label="Silver curling strip of movie film"></div>
    </section>
  </main>
</body>
</html>
```